Redesign of page from emergency manual

Please redesign this PDF to look better. Please don't include any stock photos. It must be legible. Making some words bold is probably a good idea.

Here are some things I like :

https://tarrowbooks.com.au/collections/frontpage/products/the-plk-v2-ebook

https://img-cd.vostramediafiles.com/qa-ejkwPLOTYY_SuCKbZNu411Qwgjv8YssPxEdzXN93hDkSRjLXK8WmfgbmrJW4ZZ3yUPK=w1052-h592-rw

```html
<!DOCTYPE html>
<html lang="en">
<head>
<meta charset="utf-8">
<title>Hypertension Acute</title>
<link rel="stylesheet" href="https://fonts.googleapis.com/css2?family=Montserrat:wght@400;500;600;700;800&display=swap">
<style>
  :root {
    --brand-blue: #25479b;
    --brand-tint: #e8edf8;
    --brand-soft: #f4f6fb;
    --alert: #b3261e;
    --ink: #2b2b2b;
    --rule: #2b2b2b;
    --paper: #ffffff;
  }
  * { box-sizing: border-box; margin: 0; padding: 0; }
  html, body { width: 1200px; height: 902px; overflow: hidden; background: var(--paper); }
  body { font-family: "Montserrat", sans-serif; color: var(--ink); }
  strong, b { font-weight: 700; }
  .page { position: relative; width: 1200px; height: 902px; }

  .masthead { position: absolute; left: 42px; top: 46px; width: 1116px; height: 194px; background: var(--brand-blue); }
  .masthead-title { position: absolute; left: 18px; top: 38px; color: #fff; font-weight: 800; font-size: 51px; line-height: 1.12; letter-spacing: 0.5px; }
  .masthead-tagline { position: absolute; left: 634px; top: 52px; width: 464px; height: 75px; background: #fff; color: var(--brand-blue); font-weight: 700; font-size: 19px; line-height: 1.5; display: flex; align-items: center; justify-content: center; text-align: center; }

  .causes { position: absolute; left: 58px; top: 256px; width: 665px; font-size: 16px; line-height: 32px; }
  .causes .lead-dot { display: inline-block; width: 9px; height: 9px; border-radius: 50%; background: var(--ink); margin: 0 12px 2px 8px; vertical-align: middle; }
  .causes ul { list-style: none; padding-left: 12px; }
  .causes li { position: relative; padding-left: 14px; }
  .causes li::before { content: "-"; position: absolute; left: 0; font-weight: 800; }
  .causes li.sub { margin-left: 10px; }

  .caution { position: absolute; left: 58px; top: 422px; width: 650px; height: 100px; background: var(--brand-blue); color: #fff; font-size: 15px; line-height: 21.5px; padding: 8px 12px; text-align: justify; }
  .caution strong { font-weight: 800; }

  table { border-collapse: collapse; position: absolute; }
  .bp-table { left: 733px; top: 262px; width: 408px; border: 2px solid var(--rule); font-size: 16px; }
  .bp-table caption { display: none; }
  .bp-table th.band { background: var(--brand-blue); color: #fff; height: 45px; font-weight: 700; font-size: 16.5px; }
  .bp-table th.col { height: 41px; font-weight: 700; border: 1px solid var(--rule); background: var(--brand-tint); }
  .bp-table td { height: 58px; text-align: center; border: 1px solid var(--rule); }
  .bp-table td.age { font-weight: 600; }
  .bp-table tr.alt td { background: var(--brand-soft); }

  .drug-table { left: 58px; top: 546px; width: 820px; border: 2px solid var(--rule); font-size: 15.5px; line-height: 1.5; }
  .drug-table th { background: var(--brand-blue); color: #fff; height: 38px; font-weight: 700; font-size: 17px; border-left: 2px solid #fff; }
  .drug-table th:first-child { border-left: none; width: 214px; }
  .drug-table td { border: 1px solid var(--rule); padding: 4px 12px; vertical-align: middle; }
  .drug-table td.action { font-weight: 600; color: var(--brand-blue); }
  .drug-table tr.alt td { background: var(--brand-soft); }
  .drug-table .row-smooth td { height: 65px; }
  .drug-table .row-beta td { height: 100px; }
  .drug-table .row-ccb td { height: 65px; }
  .drug-table .row-d1 td { height: 44px; }
  .indent { padding-left: 14px; display: inline-block; }

  .differential { position: absolute; left: 894px; top: 546px; width: 246px; font-size: 15px; line-height: 23.4px; }
  .differential h2 { font-size: 15.5px; font-weight: 700; color: var(--brand-blue); margin-bottom: 1px; }
  .differential ul { list-style: none; }
  .revision { position: absolute; left: 894px; top: 830px; width: 247px; height: 27px; background: var(--brand-blue); color: #fff; font-size: 16px; text-align: center; line-height: 27px; letter-spacing: 0.5px; }
</style>
</head>
<body>
<main class="page">
  <header class="masthead">
    <h1 class="masthead-title">HYPERTENSION<br>ACUTE</h1>
    <div class="masthead-tagline">Sustained high blood pressure refractory<br>to treating reversible causes</div>
  </header>

  <section class="causes">
    <p><span class="lead-dot"></span>In pediatrics, hypertension is almost always treated by <strong>addressing likely causes</strong> such as <strong>light anesthesia</strong> or <strong>measurement error</strong>:</p>
    <ul>
      <li>Ensure correct <strong>BP cuff size</strong>: cuff bladder width ~40% of limb circumference</li>
      <li>Ensure <strong>arterial line transducer</strong> is at level of heart</li>
      <li class="sub">Consider placing arterial line if not already present</li>
    </ul>
  </section>

  <aside class="caution"><strong>*CAUTION:</strong> Anti-hypertensive drugs are <strong>almost never needed</strong> for routine pediatric cases. These medications are used almost exclusively for specialized cardiac, neurosurgical, or endocrine (pheochromocytoma) cases. <strong>Consult an expert before use. Rule out increased ICP.</strong></aside>

  <table class="bp-table">
    <caption>Hypertensive blood pressure range</caption>
    <tr><th class="band" colspan="3">Hypertensive Blood Pressure Range*</th></tr>
    <tr><th class="col">Age (yr)</th><th class="col">Systolic</th><th class="col">Diastolic</th></tr>
    <tr><td class="age">Newborn</td><td>&gt;97</td><td>&gt;70</td></tr>
    <tr class="alt"><td class="age">1-3</td><td>&gt;105</td><td>&gt;62</td></tr>
    <tr><td class="age">4-12</td><td>&gt;113</td><td>&gt;86</td></tr>
  </table>

  <table class="drug-table">
    <tr><th>Action</th><th>Drug (IV Dosing)</th></tr>
    <tr class="row-smooth"><td class="action">Direct smooth muscle relaxation</td><td>- <b>Sodium nitroprusside</b> 0.5-10 MICROgrams/kg/min<br>- <b>HydrALAZINE</b> 0.1-0.2 mg/kg (adult dose 5-10 mg)</td></tr>
    <tr class="row-beta alt"><td class="action">β-Adrenergic blockade</td><td>- <b>Esmolol</b> 100-500 MICROgrams/kg/min,<br><span class="indent">then 25-300 MICROgrams/kg/min</span><br>- <b>Labetalol</b> (also α effect) 0.2-1 mg/kg q 10 min; 0.4-3 mg/kg/hour (infusion)</td></tr>
    <tr class="row-ccb"><td class="action">Calcium channel blockade</td><td>- <b>niCARdapine</b> 0.5-5 MICROgrams/kg/min<br>- <b>Clevidipine</b> 0.5-3.5 MICROgrams/kg/min</td></tr>
    <tr class="row-d1 alt"><td class="action">D1-dopamine agonist</td><td>- <b>Fenoldopam</b> 0.2-0.8 MICROgrams/kg/min</td></tr>
  </table>

  <section class="differential">
    <h2>Consider Differential (Partial):</h2>
    <ul>
      <li>- <b>Light anesthesia</b> (consider vaporizer or infusion pump empty or malfunctioning)</li>
      <li>- <b>Hypercarbia</b></li>
      <li>- <b>Hypoxemia</b></li>
      <li>- Arterial line transducer too low or BP cuff too small</li>
      <li>- <b>Withdrawal</b> (EtOH or opioid)</li>
      <li>- <b>Thyroid storm</b></li>
      <li>- <b>Pheochromocytoma</b></li>
      <li>- <b>Drug error</b></li>
    </ul>
  </section>

  <div class="revision">Revision Feb 2020</div>
</main>
</body>
</html>
```